Bauzaunbanner
Zielgruppe
Verkehrssicherungsfirma aus Neckarsulm, wir Sperren Straßen, richten Haltverbotszonen etc. ein.
Aufgabenstellung
Wir wollen Bauzaunbanner 340x173cm.
nicht zu viel Text, Leistungen sollen abbildbar sein. Wir benötigen 2-3 verschiedene Druckvorlagen, da wir die Banner nebeneinander aufhängen wollen.

```html
<!DOCTYPE html>
<html lang="de">
<head>
<meta charset="utf-8">
<title>Bauzaunbanner – Talwerk Absperrdienst</title>
<link rel="stylesheet" href="https://fonts.googleapis.com/css2?family=Archivo:wght@800&family=Lato:wght@700&display=swap">
<style>
  :root {
    --amber: #fdae00;
    --signal-red: #eb3434;
    --ink: #111111;
    --paper: #ffffff;
    --backdrop: #e4e4e4;
    --stripe-dark: #1a1a1a;
  }
  * { box-sizing: border-box; margin: 0; padding: 0; }
  html, body { width: 1200px; height: 1200px; overflow: hidden; }
  body { background: var(--backdrop); position: relative; font-family: "Lato", sans-serif; }

  .banner { position: absolute; left: 264px; width: 672px; height: 341px; overflow: hidden; }
  .banner--amber { background: var(--amber); }
  .banner--white { background: var(--paper); }
  .banner--service { top: 32px; }
  .banner--closure { top: 422px; }
  .banner--parking { top: 810px; }

  .brand {
    position: absolute; top: 30px; left: 0; right: 0;
    display: flex; justify-content: center; align-items: center; gap: 8px;
    font-family: "Archivo", sans-serif; font-weight: 800; font-size: 17px;
    color: var(--signal-red); letter-spacing: 0.02em; text-transform: uppercase;
  }
  .brand__square { width: 16px; height: 16px; background: var(--signal-red); }

  .title-band { position: absolute; left: 72px; right: 0; height: 79px; }
  .title-band--white { background: var(--paper); }
  .title-band--amber { background: var(--amber); }

  .title {
    position: absolute; top: 0; height: 100%; display: flex; align-items: center; justify-content: center;
    font-family: "Archivo", sans-serif; font-weight: 800; font-size: 40px; color: var(--ink); white-space: nowrap;
  }

  .no-entry { position: absolute; width: 106px; height: 106px; border-radius: 50%; background: var(--signal-red); }
  .no-entry::after {
    content: ""; position: absolute; left: 31px; top: 46px; width: 44px; height: 14px;
    border-radius: 3px; background: var(--paper);
  }

  .tagline {
    position: absolute; transform: translateX(-50%);
    font-weight: 700; font-size: 22px; color: var(--ink); white-space: nowrap;
  }

  .hazard-strip { position: absolute; left: 0; right: 0; bottom: 0; height: 78px; }
  .hazard-strip--black { background: linear-gradient(90deg, var(--stripe-dark), #3a2a00 50%, var(--stripe-dark)); }
  .hazard-strip--red { background: linear-gradient(90deg, var(--signal-red), #f37a7a 50%, var(--signal-red)); }
</style>
</head>
<body>

<section class="banner banner--amber banner--service">
  <div class="brand"><span class="brand__square"></span>Talwerk Absperrdienst</div>
  <div class="title-band title-band--white" style="top:103px">
    <h2 class="title" style="left:60px; right:0">VERKEHRSSICHERUNG</h2>
  </div>
  <div class="no-entry" style="left:21px; top:86px"></div>
  <p class="tagline" style="left:336px; top:208px">vom Profi</p>
  <div class="hazard-strip hazard-strip--black" role="img" aria-label="Schwarz-gelbe Warnpfeil-Markierung"></div>
</section>

<section class="banner banner--white banner--closure">
  <div class="brand"><span class="brand__square"></span>Talwerk Absperrdienst</div>
  <div class="title-band title-band--amber" style="top:110px">
    <h2 class="title" style="left:40px; right:0">STRASSENSPERRUNG</h2>
  </div>
  <div class="no-entry" style="left:33px; top:96px"></div>
  <p class="tagline" style="left:352px; top:203px">inkl. Planung</p>
  <div class="hazard-strip hazard-strip--red" role="img" aria-label="Rot-weiße Warnpfeil-Markierung"></div>
</section>

<section class="banner banner--amber banner--parking">
  <div class="brand"><span class="brand__square"></span>Talwerk Absperrdienst</div>
  <div class="title-band title-band--white" style="top:102px">
    <h2 class="title" style="left:40px; right:0">HALTVERBOT</h2>
  </div>
  <div class="no-entry" style="left:41px; top:89px"></div>
  <p class="tagline" style="left:336px; top:193px">schnell eingerichtet</p>
  <div class="hazard-strip hazard-strip--black" role="img" aria-label="Schwarz-gelbe Warnpfeil-Markierung"></div>
</section>

</body>
</html>
```